Brightpath Tutors Homepage and Landing Page Redesign

Brightpath Tutors 456 is a premier test preparation, academic consultation, and private tutoring company based in Los Angeles. We offer our tutoring in-person and also online. <br/><br/>We will need three mockups that are as follows:<br/><br/>1. A mockup of a homepage that will be on www.brightpathtutors456.com<br/>2. A mockup of a free-standing true landing page that will be a one-page site where we will direct traffic from a Zindle PPC ad.<br/>3. A mockup of a landing page that will replace a landing page such as the one at www.brightpathtutors456.com/test-prep-services/k-12/sat/ <br/><br/>Please see the word attached for details.

Target Market(s)

Middle School and High School Student Parents, College Students.

Industry/Entity Type

Tutoring

Number of Pages Required

3 page

Colors

Designer to choose colors to be used in the design.

Requirements
Must have
• The design of these 3 pages will need to fit within the overall design of the main website. We're looking for a user-friendly, easy-to-navigate, yet professional design.

```html
<!DOCTYPE html>
<html lang="en">
<head>
<meta charset="utf-8">
<title>Brightpath Tutors – Home</title>
<link href="https://fonts.googleapis.com/css2?family=Oswald:wght@400;500;600&family=Lato:wght@400;700&display=swap" rel="stylesheet">
<style>
:root{
  --teal-deep:#165b5e;
  --teal:#1e6d70;
  --teal-card:#2a8589;
  --yellow:#f6d42c;
  --lime:#b8d432;
  --orange:#ef7a4d;
  --cyan:#2ec6ec;
  --ink:#1c1c1c;
  --muted:#6c6c6c;
  --panel:#f1f1f1;
  --line:#e4e4e4;
  --white:#ffffff;
}
*{box-sizing:border-box;margin:0;padding:0}
html,body{width:1200px;height:3932px;overflow:hidden;background:var(--white)}
body{position:relative;font-family:'Lato',sans-serif;color:var(--ink)}
.abs{position:absolute}
.display{font-family:'Oswald',sans-serif;font-weight:500;letter-spacing:-.3px}
.btn{position:absolute;display:flex;align-items:center;justify-content:center;font-family:'Oswald',sans-serif;font-weight:500;font-size:16px;text-decoration:none}
.btn-teal{background:var(--teal);color:var(--white)}
.btn-yellow{background:var(--yellow);color:var(--teal)}
.btn-ghost{background:var(--white);color:var(--teal);border:2px solid var(--teal)}

/* hero */
.hero{left:0;top:0;width:1200px;height:638px;border-radius:0 0 90px 90px;overflow:hidden;
  background:linear-gradient(100deg,#123f42 0%,#1a5f62 45%,#1f6b6e 100%)}
.brand{color:var(--white);font-family:'Oswald',sans-serif;font-weight:600;font-size:28px;line-height:1;letter-spacing:.5px;white-space:nowrap}
.nav{top:30px;left:515px;display:flex;gap:18px;font-size:11px;font-weight:700;color:var(--white)}
.hero h1{left:163px;top:190px;font-size:64px;line-height:60px;color:var(--white)}
.hero p{left:163px;top:330px;width:470px;font-size:13px;line-height:23px;color:#e6eeee}
.hero-photo{left:690px;top:92px;width:405px;height:475px;border-radius:200px 200px 160px 160px;
  background:radial-gradient(ellipse at 50% 40%,#e24a3a 0%,#c8473d 35%,#4f7595 70%,rgba(31,107,110,0) 100%)}

/* services */
.section-title{width:1200px;left:0;text-align:center;font-size:38px}
.section-sub{left:420px;width:360px;text-align:center;font-size:11.5px;line-height:20px;color:var(--muted)}
.svc{top:837px;width:202px;height:224px;background:var(--white);border:1px solid var(--line);box-shadow:0 2px 8px rgba(0,0,0,.08);border-radius:4px;padding:28px 12px 0 14px}
.svc.featured{background:var(--teal-card);border-color:var(--teal-card);color:var(--white)}
.svc h3{font-family:'Oswald',sans-serif;font-weight:400;font-size:15.5px;line-height:22px;text-transform:uppercase;width:110px}
.svc p{margin-top:20px;font-size:11px;line-height:19.5px;color:var(--muted)}
.svc.featured p{color:#e3f0f0}
.svc svg{position:absolute;right:16px;top:24px}
.svc .btn{left:14px;top:158px;width:105px;height:36px}

/* results */
.results{left:0;top:1153px;width:1200px;height:673px;background:var(--panel);border-radius:60px}
.results h2{left:163px;top:195px;font-size:34px;line-height:37px;width:290px}
.results p{left:163px;top:323px;width:275px;font-size:11px;line-height:19.5px;color:var(--muted)}
.stat{width:202px;height:225px;background:var(--white);border-radius:4px;box-shadow:0 2px 8px rgba(0,0,0,.05);text-align:center}
.stat svg{position:absolute;left:52px;top:22px}
.stat .num{position:absolute;left:0;top:54px;width:202px;font-family:'Oswald',sans-serif;font-weight:500;font-size:28px}
.stat h4{position:absolute;left:0;top:130px;width:202px;font-family:'Oswald',sans-serif;font-weight:500;font-size:18px}
.stat p{position:absolute;left:18px;top:160px;width:166px;font-size:11px;line-height:19.5px;color:var(--muted)}

/* steps */
.step{color:var(--white);font-family:'Oswald',sans-serif;font-weight:500;font-size:15px;line-height:22px;padding:16px 10px;border-radius:3px;box-shadow:0 6px 14px rgba(0,0,0,.12)}
.step svg{position:absolute}
.easy h2{right:162px;top:1928px;font-size:38px}
.easy p{left:762px;top:1990px;width:277px;text-align:right;font-size:11px;line-height:19.5px;color:var(--muted)}

/* tutors */
.tutor{top:2451px;width:238px;height:279px;background:var(--white);border:1px solid var(--line);border-radius:6px;text-align:center}
.tutor .photo{position:absolute;left:7px;top:7px;width:224px;height:164px;background:linear-gradient(180deg,#e4ecee 0%,#d4e0e3 100%)}
.tutor h5{position:absolute;top:192px;width:100%;font-family:'Oswald',sans-serif;font-weight:400;font-size:15px}
.tutor .spec{position:absolute;top:216px;width:100%;font-size:10px;font-weight:700;color:var(--teal)}
.tutor .cred{position:absolute;top:234px;width:100%;font-size:11px;line-height:19.5px;color:var(--muted)}

/* consultation */
.consult{left:162px;top:2897px;width:876px;height:485px;background:var(--panel);border-radius:30px;overflow:hidden}
.grads{left:0;top:96px;width:357px;height:389px;background:linear-gradient(180deg,#2b2b2e 0%,#3a3438 55%,#d8c4b4 100%);border-radius:160px 160px 0 0}
.consult h2{left:406px;top:54px;font-size:33px}
.consult .lead{left:406px;top:100px;width:420px;font-size:11px;line-height:19.5px;color:var(--muted)}
.field{position:absolute;background:var(--white);border:1px solid #e3e3e3;font-size:10px;color:#777;padding:14px 14px}

/* footer */
.footer{left:0;top:3452px;width:1200px;height:449px;background:var(--teal);border-radius:75px 75px 0 0;color:var(--white)}
.footer-nav{top:130px;left:0;width:1200px;display:flex;justify-content:center;gap:25px;font-size:11px}
.footer-rule{left:162px;top:167px;width:876px;height:1px;background:rgba(255,255,255,.3)}
.fcol{top:198px}
.fcol h6{font-family:'Oswald',sans-serif;font-weight:500;font-size:15px;color:var(--yellow);margin-bottom:16px}
.fcol li{list-style:none;font-size:11px;line-height:19.5px}
.contact-row{position:absolute;left:40px;font-size:11px;line-height:19.5px;white-space:nowrap}
.contact-row svg{position:absolute;left:-40px;top:0}
.copyright{left:0;top:3901px;width:1200px;height:31px;background:var(--yellow);text-align:center;font-size:11px;line-height:31px;color:var(--ink)}
</style>
</head>
<body>

<!-- Hero -->
<header class="abs hero">
  <div class="abs brand" style="left:163px;top:22px">BRIGHTPATH TUTORS</div>
  <nav class="abs nav">
    <span>Home</span><span>About</span><span>Academic Support</span><span>Test Prep</span><span>Resources</span><span>Contact</span>
  </nav>
  <a class="btn btn-yellow" style="left:927px;top:18px;width:111px;height:37px;font-size:15px">310 555 0147</a>
  <div class="abs hero-photo" role="img" aria-label="Smiling student sitting cross-legged with notebooks and a pencil"></div>
  <h1 class="abs display">A Place Where You<br>Can Achieve</h1>
  <p class="abs">Experienced, Professional Tutors Available For Private Sessions Either In-Home In Los Angeles Or Online, Worldwide.</p>
  <a class="btn btn-yellow" style="left:162px;top:397px;width:224px;height:53px;font-size:19px">Get A Free Consulting</a>
</header>

<!-- Services -->
<h2 class="abs display section-title" style="top:708px">Our Services</h2>
<p class="abs section-sub" style="top:764px">Lorem Ipsum is simply dummy text of the printing and typesetting industry. Lorem Ipsum has been the text.</p>

<div class="abs svc featured" style="left:162px">
  <h3>Academic Tutoring</h3>
  <svg width="50" height="50" viewBox="0 0 50 50" fill="none" stroke="#fff" stroke-width="1.6"><rect x="6" y="8" width="26" height="20"/><path d="M10 14h18M10 19h12M20 28v10M12 40h32M36 14c4 0 7 3 7 7s-3 7-7 7-7-3-7-7"/><circle cx="38" cy="34" r="4"/></svg>
  <p>Work with one of our expert tutors to supplement what you're learning in school. We will help you stay on track or even push you to stay ahead of the game...</p>
</div>
<div class="abs svc" style="left:385px">
  <h3>K-12 / College Test Prep</h3>
  <svg width="44" height="48" viewBox="0 0 44 48" fill="none" stroke="#1e6d70" stroke-width="1.6"><rect x="4" y="4" width="28" height="38"/><path d="M10 34h16M10 38h12"/><circle cx="20" cy="18" r="8"/><path d="M26 24l12 12"/></svg>
  <p>Work one-on-one with one of our veteran tutors to help you achieve your test prep goals.</p>
  <a class="btn btn-teal">Read More</a>
</div>
<div class="abs svc" style="left:611px">
  <h3>Graduate Test Prep</h3>
  <svg width="46" height="48" viewBox="0 0 46 48" fill="none" stroke="#1e6d70" stroke-width="1.6"><path d="M6 14l20-8 18 8-18 8z"/><path d="M14 18v8c4 3 14 3 18 0v-8M40 16v10"/><path d="M6 44l14-14 4 4-14 14z"/></svg>
  <p>Prepare for your graduate-level exam with one of our experienced tutors and customize.</p>
  <a class="btn btn-teal">Read More</a>
</div>
<div class="abs svc" style="left:835px">
  <h3>Professional Test Prep</h3>
  <svg width="48" height="44" viewBox="0 0 48 44" fill="none" stroke="#1e6d70" stroke-width="1.6"><rect x="4" y="4" width="40" height="32"/><path d="M4 10h40M10 16h12M10 22h8M26 16h12M26 22h12M26 28h8M18 40h12"/></svg>
  <p>Connect with a specialist who can work around your availability and help you pass your unique.</p>
  <a class="btn btn-teal">Read More</a>
</div>

<!-- Results -->
<section class="abs results">
  <h2 class="abs display">Proven Results From a Tutoring Company You Can Trust</h2>
  <p class="abs">Brightpath Tutors only works with highly experienced, professional, veteran tutors who have a proven track record of success. Our individualized approach has helped countless students achieve the academic and test prep goals of their dreams.</p>
  <a class="btn btn-teal" style="left:162px;top:447px;width:111px;height:36px">Read More</a>

  <div class="abs stat" style="left:551px;top:88px">
    <svg width="98" height="98" viewBox="0 0 98 98"><circle cx="49" cy="49" r="46" fill="none" stroke="#e6e6e6" stroke-width="3"/><circle cx="49" cy="49" r="46" fill="none" stroke="var(--orange)" stroke-width="3" stroke-dasharray="260 289" transform="rotate(-80 49 49)"/></svg>
    <div class="num" style="color:var(--orange)">150</div>
    <h4>SAT</h4>
    <p>Our students average a 150 point increase on the SAT.</p>
  </div>
  <div class="abs stat" style="left:776px;top:134px">
    <svg width="98" height="98" viewBox="0 0 98 98"><circle cx="49" cy="49" r="46" fill="none" stroke="#e6e6e6" stroke-width="3"/><circle cx="49" cy="49" r="46" fill="none" stroke="var(--cyan)" stroke-width="3" stroke-dasharray="260 289" transform="rotate(-90 49 49)"/></svg>
    <div class="num" style="color:var(--cyan)">90%</div>
    <h4>CSET</h4>
    <p>Over 90% of our students pass the CSET.</p>
  </div>
  <div class="abs stat" style="left:551px;top:337px">
    <svg width="98" height="98" viewBox="0 0 98 98"><circle cx="49" cy="49" r="46" fill="none" stroke="#e6e6e6" stroke-width="3"/><circle cx="49" cy="49" r="46" fill="none" stroke="var(--teal)" stroke-width="3" stroke-dasharray="175 289" transform="rotate(-90 49 49)"/></svg>
    <div class="num" style="color:var(--teal)">4</div>
    <h4>ACT</h4>
    <p>Our students average a 4 point increase on the ACT.</p>
  </div>
  <div class="abs stat" style="left:776px;top:382px">
    <svg width="98" height="98" viewBox="0 0 98 98"><circle cx="49" cy="49" r="46" fill="none" stroke="#e6e6e6" stroke-width="3"/><circle cx="49" cy="49" r="46" fill="none" stroke="var(--yellow)" stroke-width="3" stroke-dasharray="80 289" transform="rotate(-90 49 49)"/></svg>
    <div class="num" style="color:var(--yellow)">2.5</div>
    <h4>ISEE</h4>
    <p>Our students average a 2.5 stanine improvement on the ISEE.</p>
  </div>
</section>

<!-- Easy as 1-2-3 -->
<div class="abs step" style="left:266px;top:1945px;width:157px;height:179px;background:var(--teal-card)">
  Answer A Few Questions About Your Needs
  <svg style="left:88px;top:118px" width="44" height="46" viewBox="0 0 44 46" fill="none" stroke="#fff" stroke-width="1.5"><rect x="4" y="4" width="30" height="38"/><path d="M10 12h18M10 18h18M10 24h18M10 30h12M34 10h6v34H10"/></svg>
</div>
<div class="abs step" style="left:438px;top:1900px;width:112px;height:125px;background:var(--yellow);padding:8px 10px">
  Schedule Your First Session
  <svg style="left:50px;top:68px" width="48" height="46" viewBox="0 0 48 46" fill="none" stroke="#222" stroke-width="1.5"><rect x="4" y="6" width="40" height="36"/><path d="M4 14h40M12 2v8M36 2v8M10 20h28M10 26h28M10 32h28M18 14v28M28 14v28"/></svg>
</div>
<div class="abs step" style="left:440px;top:2042px;width:149px;height:161px;background:var(--cyan);padding:12px 12px">
  We Match You With The Perfect Tutor
  <svg style="left:80px;top:98px" width="48" height="44" viewBox="0 0 48 44" fill="none" stroke="#fff" stroke-width="1.5"><rect x="4" y="4" width="40" height="28"/><path d="M18 40h12M24 32v8"/><circle cx="18" cy="14" r="4"/><path d="M12 26c1-5 11-5 12 0M30 12h8M30 18h8M30 24h6"/></svg>
</div>
<div class="easy">
  <h2 class="abs display">It's As Easy as 1-2-3</h2>
  <p class="abs">Lorem Ipsum is simply dummy text of the printing and typesetting industry. Lorem Ipsum has been the industry's standard dummy text ever since the 1500s, when an unknown printer took a galley of type and scrambled it to make a type specimen book.</p>
</div>
<a class="btn btn-teal" style="left:799px;top:2121px;width:113px;height:36px">Enroll Today</a>
<a class="btn btn-ghost" style="left:927px;top:2121px;width:111px;height:36px">Learn More</a>

<!-- Tutors -->
<h2 class="abs display section-title" style="top:2308px">Our Tutors</h2>
<p class="abs section-sub" style="top:2367px">Lorem Ipsum is simply dummy text of the printing and typesetting industry. Lorem Ipsum has been the text.</p>

<div class="abs tutor" style="left:226px">
  <div class="photo" role="img" aria-label="Portrait of tutor Owen R. in a dark suit"></div>
  <h5>OWEN R.</h5>
  <div class="spec">Specializes in ISEE</div>
  <div class="cred">Pacific Institute of Science<br>Ph.D. candidate</div>
</div>
<div class="abs tutor" style="left:481px">
  <div class="photo" role="img" aria-label="Portrait of tutor Clara M. smiling"></div>
  <h5>CLARA M.</h5>
  <div class="spec">Specializes in ACT</div>
  <div class="cred">Northfield College<br>B.E in Mechanical Engineering</div>
</div>
<div class="abs tutor" style="left:736px">
  <div class="photo" role="img" aria-label="Portrait of tutor Julian P. in a blue shirt"></div>
  <h5>JULIAN P.</h5>
  <div class="spec">Specializes in HSPT</div>
  <div class="cred">Eastbrook University<br>B.A. in Literature</div>
</div>
<a class="btn btn-teal" style="left:544px;top:2788px;width:113px;height:37px">More Tutors</a>

<!-- Consultation -->
<section class="abs consult">
  <div class="abs grads" role="img" aria-label="Two graduates in caps and gowns holding diplomas"></div>
  <h2 class="abs display">Schedule a Free Consultation Today</h2>
  <p class="abs lead">Our elite team of tutors has been helping students realize their academic potential for over a decade. Let us do the same for you.</p>
  <div class="field" style="left:406px;top:146px;width:214px;height:40px">Name:</div>
  <div class="field" style="left:637px;top:146px;width:216px;height:40px">Phone:</div>
  <div class="field" style="left:406px;top:200px;width:214px;height:39px">School Name:</div>
  <div class="field" style="left:637px;top:200px;width:216px;height:39px">HomeZip Code:</div>
  <div class="field" style="left:406px;top:253px;width:447px;height:40px">Email:</div>
  <div class="field" style="left:406px;top:305px;width:447px;height:74px">Message:</div>
  <a class="btn btn-teal" style="left:404px;top:401px;width:112px;height:38px">Drop A Mail</a>
</section>

<!-- Footer -->
<footer class="abs footer">
  <div class="abs brand" style="left:0;top:70px;width:1200px;text-align:center;font-size:30px">BRIGHTPATH TUTORS</div>
  <nav class="abs footer-nav">
    <span>Home</span><span>About Us</span><span>Academic Support</span><span>Test Prep</span><span>Resources</span><span>Contact Us</span>
  </nav>
  <div class="abs footer-rule"></div>
  <div class="abs fcol" style="left:163px">
    <h6>More Info</h6>
    <ul><li>Tutoring Resources</li><li>FAQ</li><li>Blog</li><li>Tutoring Jobs</li><li>Innovation Scholarship</li><li>Free Diagnostic Test</li></ul>
  </div>
  <div class="abs fcol" style="left:388px">
    <h6>Services</h6>
    <ul><li>SAT</li><li>ACT</li><li>ISEE</li><li>CHSPE</li><li>GMAT</li><li>CSET</li></ul>
  </div>
  <div class="abs fcol" style="left:602px;width:230px">
    <h6>Contact Us</h6>
    <div class="contact-row" style="top:40px">
      <svg width="24" height="22" viewBox="0 0 24 22" fill="none" stroke="var(--yellow)" stroke-width="2"><path d="M5 3l4 1 1 5-3 2c1 3 3 5 6 6l2-3 5 1 1 4c-9 2-18-7-16-16z"/></svg>
      310-555-0147
    </div>
    <div class="contact-row" style="top:85px">
      <svg width="24" height="20" viewBox="0 0 24 20"><rect x="1" y="3" width="22" height="15" fill="var(--yellow)"/><path d="M1 3l11 8 11-8" fill="none" stroke="var(--teal)" stroke-width="2"/></svg>
      hello@brightpathtutors456.com
    </div>
    <div class="contact-row" style="top:130px">
      <svg width="24" height="30" viewBox="0 0 24 30"><path d="M12 1C6 1 2 5 2 11c0 7 10 17 10 17s10-10 10-17C22 5 18 1 12 1z" fill="var(--yellow)"/><circle cx="12" cy="11" r="4" fill="var(--teal)"/></svg>
      1820 Marlow Ave.<br>Suite 300, Beverly Hills, CA 90211
    </div>
  </div>
  <div class="abs fcol" style="left:838px;width:200px">
    <h6>Newsletter</h6>
    <p style="font-size:11px;line-height:19.5px">Subscribe our newsletter and get latest updates &amp; News</p>
    <div class="field" style="left:0;top:96px;width:194px;height:35px;padding:10px 12px">Enter Email:</div>
    <a class="btn btn-yellow" style="left:-2px;top:142px;width:113px;height:36px;font-size:14px">Subscribe Now</a>
  </div>
</footer>
<div class="abs copyright">Copyright © 2020 Brightpath Tutors 456 - All Rights Reserved. Terms &amp; Conditions | Privacy Policy.</div>

</body>
</html>
```